Business Card Design

I am a Building Surveyor and run my own Building Consultat company, providing professional advice and services to builders, architects, designers, owners, etc.

Industry/Entity Type

Business

Contact Information for Business Card

Dorwen Halket BBldgSurv (Hons)
Managing Director

57 Quillon Rise, Marrick Heights WA 6148
Mobile 0438 271 594
Email Dorwen.halket@tarnwellpq.com

Requirements
Must have
• I would like the back of the business card to be one colour (a shade of either black or maroon, matching the colours of my logo). Positioned in the centre on the back of the business card is to be my logo.

The front of the card is to be white, with my contact information in either black or maroon. The ADBldgSurv after my name should be in a smaller font size than my name. I would also like a small logo somewhere on this side of the card.

```html
<!DOCTYPE html>
<html lang="en">
<head>
<meta charset="utf-8">
<title>Tarnwell Building Consultants – Business Card</title>
<link href="https://fonts.googleapis.com/css2?family=EB+Garamond:wght@400;500&display=swap" rel="stylesheet">
<style>
  :root {
    --page: #d9d6d2;
    --maroon: #6e1a12;
    --maroon-deep: #2e0804;
    --maroon-mid: #5a140c;
    --charcoal: #4a4a4c;
    --white: #ffffff;
    --grey-edge: #b9b9b9;
    --ink: #7a1c12;
  }
  * { box-sizing: border-box; margin: 0; padding: 0; }
  html, body { width: 1200px; height: 1000px; overflow: hidden; }
  body {
    background: var(--page);
    position: relative;
    font-family: "EB Garamond", Georgia, serif;
  }
  .card {
    position: absolute;
    width: 740px;
    height: 450px;
    overflow: hidden;
    box-shadow: 0 10px 26px rgba(0,0,0,0.35);
  }

  /* Back of card */
  .card--back {
    left: 40px; top: 50px;
    background: radial-gradient(ellipse at 55% 45%, var(--maroon) 0%, var(--maroon-mid) 45%, var(--maroon-deep) 100%);
  }
  .card--back .ghost-ring {
    position: absolute;
    left: 230px; top: 30px;
    width: 390px; height: 390px;
    border-radius: 50%;
    border: 26px solid rgba(255,255,255,0.07);
  }
  .card--back .band {
    position: absolute;
    left: 0; right: 0;
    top: 150px; height: 118px;
    background: var(--white);
    display: flex;
    align-items: center;
    padding-left: 70px;
    gap: 26px;
  }
  .mark-dot {
    border-radius: 50%;
    background: var(--maroon);
    flex: none;
  }
  .card--back .mark-dot { width: 78px; height: 78px; }
  .wordmark {
    color: var(--charcoal);
    font-weight: 500;
    text-transform: uppercase;
    line-height: 1;
  }
  .card--back .wordmark__name { font-size: 66px; letter-spacing: 2px; display: block; }
  .card--back .wordmark__line { font-size: 22px; letter-spacing: 3px; display: block; margin-top: 6px; padding-left: 100px; }

  /* Front of card */
  .card--front {
    left: 420px; top: 500px;
    background: radial-gradient(ellipse at 50% 50%, var(--white) 40%, #ececec 70%, var(--grey-edge) 100%);
  }
  .card--front .band {
    position: absolute;
    left: 0; right: 0;
    top: 160px; height: 140px;
    background: var(--white);
  }
  .person {
    position: absolute;
    left: 90px; top: 205px;
    color: var(--ink);
    text-align: right;
  }
  .person__name { font-size: 34px; font-weight: 400; display: block; line-height: 1; }
  .person__title { font-size: 20px; display: block; margin-top: 8px; }
  .contact {
    position: absolute;
    left: 395px; top: 182px;
    color: var(--ink);
    font-size: 18px;
    line-height: 1.2;
    list-style: none;
  }
  .front-logo {
    position: absolute;
    left: 240px; top: 272px;
    display: flex;
    align-items: center;
    gap: 12px;
  }
  .front-logo .mark-dot { width: 44px; height: 44px; }
  .front-logo .wordmark__name { font-size: 30px; letter-spacing: 1px; display: block; }
  .front-logo .wordmark__line { font-size: 11px; letter-spacing: 1.5px; display: block; margin-top: 2px; padding-left: 40px; }
</style>
</head>
<body>
  <section class="card card--back" aria-label="Card back">
    <div class="ghost-ring" aria-hidden="true"></div>
    <div class="band">
      <span class="mark-dot" aria-hidden="true"></span>
      <p class="wordmark">
        <span class="wordmark__name">Tarnwell</span>
        <span class="wordmark__line">Building Consultants</span>
      </p>
    </div>
  </section>

  <section class="card card--front" aria-label="Card front">
    <div class="band"></div>
    <p class="person">
      <span class="person__name">Dorwen Halket</span>
      <span class="person__title">ADBldgSurv Director</span>
    </p>
    <ul class="contact">
      <li>Mobile 0438 271 594</li>
      <li>Email Dorwen.halket@tarnwellpq.com</li>
      <li>57 Quillon Rise, Marrick Heights WA 6148</li>
    </ul>
    <div class="front-logo">
      <span class="mark-dot" aria-hidden="true"></span>
      <p class="wordmark">
        <span class="wordmark__name">Tarnwell</span>
        <span class="wordmark__line">Building Consultants</span>
      </p>
    </div>
  </section>
</body>
</html>
```